Flyer / marketing email used to solicate work for specialized tree removal equipment.

I'm looking for a flyer for door to door and direct mail distributon. Please utilize as much of the following verbiage as possible...

Breaking news!¿the only 170' grapple crane in use in North American is coming to your neighborhood This revolutionary technology will be in your area for a limited time. Our equipment allows to us accomplish the most challenging tree scenarios with no climber, limited personnel, and amazing efficiency.

This innovation has completely changed the cost of hazardous removals. Call now to get the most competitive estimate yet.

This technology is so limited and in high demand that it can only be in your area for a short time before it has to move on. Get on the list today, it may be months before it makes another round to your neighborhood. ¿

Target Market(s)

Flyers will be delivered in a high end residential neighborhood. Distribution will be on heavy stock and via email.

Colors

Designer to choose colors to be used in the design.

Requirements
Must have
• My logo. Pictures of the crane equipment. Pictures of other tree equipment.
• I'd like a two sided 4" x 5.5" mailer.
• I have permissions to utilize content from the sample one fold flyers I have uploaded.
• I'd like a majority of the content of the Vortalix (aka. Plover limb sample). The light background of the 842 Boughs sample.
• A "BLACK FRIDAY SALE" theme would be awesome.
Nice to have
• Old time breaking news headline married with a high tech innovative feel
• OR
• BLACK FRIDAY SALE theme.

```html
<!DOCTYPE html>
<html lang="en">
<head>
<meta charset="utf-8">
<title>842 Boughs – Breaking News Flyer</title>
<link href="https://fonts.googleapis.com/css2?family=Exo+2:ital,wght@0,400;0,600;0,700;1,700;1,800&family=Playball&display=swap" rel="stylesheet">
<style>
  :root {
    --green: #4cb82c;
    --green-dark: #1f6a12;
    --brown: #3b1d0c;
    --brown-mid: #5a2c12;
    --ink: #1a1a1a;
    --paper: #f4f4f4;
    --white: #ffffff;
    --ring: #c9c9c9;
  }
  * { margin: 0; padding: 0; box-sizing: border-box; }
  html, body { width: 857px; height: 1200px; overflow: hidden; background: var(--paper); }
  body { font-family: "Exo 2", sans-serif; color: var(--ink); }
  .flyer { position: relative; width: 857px; height: 1200px; overflow: hidden;
    background: linear-gradient(180deg, #ffffff 0%, #ececec 100%); }
  .shapes { position: absolute; inset: 0; }

  .brand { position: absolute; left: 118px; top: 632px; width: 240px; text-align: center; }
  .brand-name { display: inline-flex; align-items: center; gap: 8px;
    font-weight: 700; font-size: 26px; line-height: 32px; color: var(--brown); }
  .brand-dot { width: 18px; height: 18px; border-radius: 50%; background: var(--green); }
  .brand-tagline { margin-top: 8px; font-family: "Playball", cursive; font-size: 16px;
    line-height: 20px; color: var(--ink); }

  .headline-tag { position: absolute; left: 92px; top: 726px; font-style: italic; font-weight: 700;
    font-size: 31px; line-height: 38px; color: var(--white); letter-spacing: 0.5px; }
  .headline-main { position: absolute; left: 106px; top: 760px; font-style: italic; font-weight: 800;
    font-size: 80px; line-height: 1; color: var(--ink); letter-spacing: -1px; }

  .news-copy { position: absolute; left: 46px; top: 856px; width: 398px; font-size: 12.2px;
    line-height: 14.1px; text-align: justify; color: #222; }

  .call-to-action { position: absolute; left: 25px; top: 1034px; width: 427px; text-align: center;
    font-weight: 700; font-size: 18px; line-height: 21px; color: var(--brown); }

  .phone-number { position: absolute; left: 160px; top: 1104px; font-weight: 600; font-size: 30px;
    line-height: 38px; color: var(--white); letter-spacing: 0.5px; }

  .why-title { position: absolute; left: 521px; top: 646px; font-weight: 700; font-size: 26px; color: var(--green); }
  .why-lead { position: absolute; left: 521px; top: 692px; width: 309px; font-weight: 700; font-size: 12.5px;
    line-height: 14px; color: var(--white); }
  .why-copy { position: absolute; left: 521px; top: 738px; width: 309px; font-size: 12.3px;
    line-height: 15.6px; text-align: justify; color: var(--white); }

  .contact-title { position: absolute; left: 481px; top: 1066px; font-weight: 600; font-size: 22px; color: var(--white); }
  .contact-line { position: absolute; left: 514px; font-size: 17px; line-height: 22px; color: var(--white); }
  .contact-email { top: 1113px; }
  .contact-web { top: 1139px; }
</style>
</head>
<body>
<main class="flyer">
  <svg class="shapes" width="857" height="1200" viewBox="0 0 857 1200" xmlns="http://www.w3.org/2000/svg">
    <defs>
      <linearGradient id="photoTones" x1="0" y1="0" x2="0" y2="1">
        <stop offset="0" stop-color="#cfe0f2"/>
        <stop offset="0.45" stop-color="#9fb7cf"/>
        <stop offset="0.7" stop-color="#4f6a3a"/>
        <stop offset="1" stop-color="#2f4a24"/>
      </linearGradient>
      <linearGradient id="brownPanel" x1="0" y1="0" x2="0" y2="1">
        <stop offset="0" stop-color="#5a2c12"/>
        <stop offset="1" stop-color="#3b1d0c"/>
      </linearGradient>
      <linearGradient id="greenPill" x1="0" y1="0" x2="1" y2="0">
        <stop offset="0" stop-color="#134d0a"/>
        <stop offset="0.5" stop-color="#3a8f1f"/>
        <stop offset="1" stop-color="#134d0a"/>
      </linearGradient>
      <linearGradient id="circleA" x1="0" y1="0" x2="0" y2="1">
        <stop offset="0" stop-color="#8fb7e0"/>
        <stop offset="0.55" stop-color="#d8cfc0"/>
        <stop offset="1" stop-color="#4a5a3c"/>
      </linearGradient>
      <linearGradient id="circleB" x1="0" y1="0" x2="0" y2="1">
        <stop offset="0" stop-color="#4f8fd6"/>
        <stop offset="0.7" stop-color="#9dc1e6"/>
        <stop offset="1" stop-color="#3d5a2e"/>
      </linearGradient>
    </defs>

    <!-- hero photo -->
    <path role="img" aria-label="Photo of a white truck with a blue grapple crane reaching over trees beside a utility pole"
      d="M0 0 H857 V370 C720 420 600 505 488 528 C330 545 160 528 0 505 Z" fill="url(#photoTones)"/>
    <path d="M0 505 C160 528 330 545 488 528" fill="none" stroke="var(--green)" stroke-width="4"/>

    <!-- why choose us panel -->
    <path d="M488 480 L857 372 V1066 L488 1021 Z" fill="url(#brownPanel)"/>
    <path d="M600 450 L857 372" stroke="var(--green)" stroke-width="6"/>

    <!-- contact panel -->
    <path d="M469 1017 L857 1063 V1200 H469 Z" fill="var(--green)"/>

    <!-- inset photo circles -->
    <circle cx="496" cy="496" r="137" fill="var(--ring)"/>
    <circle cx="496" cy="496" r="130" fill="var(--green)"/>
    <circle role="img" aria-label="Photo of a bucket truck working beside a house" cx="496" cy="496" r="124" fill="url(#circleA)"/>
    <circle cx="741" cy="439" r="100" fill="var(--ring)"/>
    <circle cx="741" cy="439" r="94" fill="var(--green)"/>
    <circle role="img" aria-label="Photo of a crane lifting a tall pine against the sky" cx="741" cy="439" r="88" fill="url(#circleB)"/>

    <!-- breaking banner -->
    <path d="M52 725 H331 L322 766 H46 Z" fill="var(--brown)"/>

    <!-- phone pill -->
    <rect x="33" y="1097" width="411" height="54" rx="27" fill="url(#greenPill)"/>
    <ellipse cx="238" cy="1161" rx="190" ry="6" fill="#000" opacity="0.12"/>
    <circle cx="117" cy="1124" r="17" fill="none" stroke="var(--white)" stroke-width="2.5"/>
    <path d="M110 1114 c-3 2 -3 8 1 13 c4 5 9 8 12 6 l2 -3 l-4 -4 l-3 2 c-2 -1 -5 -4 -6 -7 l2 -2 l-3 -5 Z" fill="var(--white)"/>

    <!-- contact icons -->
    <rect x="486" y="1118" width="18" height="13" fill="none" stroke="var(--white)" stroke-width="2"/>
    <path d="M486 1118 L495 1126 L504 1118" fill="none" stroke="var(--white)" stroke-width="2"/>
    <circle cx="495" cy="1150" r="8" fill="none" stroke="var(--white)" stroke-width="2"/>
    <ellipse cx="495" cy="1150" rx="3.5" ry="8" fill="none" stroke="var(--white)" stroke-width="1.5"/>
    <path d="M487 1150 H503" stroke="var(--white)" stroke-width="1.5"/>
  </svg>

  <div class="brand">
    <div class="brand-name"><span class="brand-dot"></span>842 Boughs</div>
    <div class="brand-tagline">Serving Central Indiana</div>
  </div>

  <div class="headline-tag">BREAKING</div>
  <div class="headline-main">NEWS</div>

  <p class="news-copy">the only 170' grapple crane in use in North American is coming to your neighborhood This revolutionary technology will be in your area for a limited time. Our equipment allows to us accomplish the most challenging tree scenarios with no climber, limited personnel, and amazing efficiency. This innovation has completely changed the cost of hazardous removals and it is so limited and in high demand that it can only be in your area for a short time before it has to move on. Get on the list today, it may be months before it makes another round to your neighborhood.</p>

  <p class="call-to-action">CALL NOW TO GET THE MOST COMPETITIVE<br>ESTIMATE YET.</p>
  <div class="phone-number">555-014-LEAF</div>

  <h2 class="why-title">WHY CHOOSE US</h2>
  <p class="why-lead">We are licensed,bonded and insured. Our<br>arborist services include:</p>
  <p class="why-copy">Tree trimming, pruning, removal, stump grinding, storm damage clean up and 24/7 emergency call services . Power lines are no problem. We specialize in trees where heavy equipment, cannot be used or no access is available. Our 35 ton crane gives us the ability to effectively complete removals that our competetion could only dream about. We have the ability to match and or beat our competitors pricing!<br>we provide free estimates. Our certified arborist ensure we are able to safety diagnose, treat, trim and remove your trees with the most urgent care and precision. All without the cause of damage to your surrounding structures, landscapes and any other property that might serve as an obstacle. Our cleanup is superior to none we leave your property looking better then before .</p>

  <h3 class="contact-title">Get In Touch With US</h3>
  <div class="contact-line contact-email">842boughs@mailbox.com</div>
  <div class="contact-line contact-web">www.842boughs.com</div>
</main>
</body>
</html>
```